Garden Design Flier

I would like a PDF of this half page A4 flier in soft green tones with dark green leaves.

Target Market(s)

Home owners and real estate agents

Font styles to use
Serif
Other font styles liked:
• Papyrus

Colors
acd136
9bcb3c
cadf82
fefdec

Requirements
Must have
• Green tones
Nice to have
• Leaves, vines, lawns
Should not have
• Open to ideas, but classic style

```html
<!DOCTYPE html>
<html lang="en">
<head>
<meta charset="utf-8">
<title>Kitchen Plot Gardens – Flier</title>
<link rel="stylesheet" href="https://fonts.googleapis.com/css2?family=Sorts+Mill+Goudy:ital@0;1&display=swap">
<style>
  :root {
    --teal: #27b8a5;
    --white: #ffffff;
    --leaf: #0f9448;
    --leaf-dark: #146236;
    --serif: "Sorts Mill Goudy", Georgia, serif;
  }
  * { margin: 0; padding: 0; box-sizing: border-box; }
  html, body { width: 1200px; height: 848px; overflow: hidden; background: var(--teal); }
  .flier {
    position: relative;
    width: 1200px;
    height: 848px;
    background: var(--teal);
    font-family: var(--serif);
    color: var(--white);
    overflow: hidden;
  }
  .foliage { position: absolute; inset: 0; }
  .frame {
    position: absolute;
    left: 27px; top: 24px; width: 1146px; height: 798px;
    border: 7px solid var(--white);
  }
  .credential {
    position: absolute;
    left: 96px; top: 64px;
    font-size: 27px;
    line-height: 37px;
    letter-spacing: 0.04em;
  }
  .credential .course { font-style: italic; }
  .credential .level { font-style: italic; }
  .credential .college {
    font-style: normal;
    font-size: 20px;
    letter-spacing: 0.06em;
    margin-left: 6px;
  }
  .steps {
    position: absolute;
    left: 978px; top: 60px;
    list-style: none;
    font-size: 29px;
    line-height: 42px;
    letter-spacing: 0.03em;
    text-shadow: 1px 2px 0 rgba(0, 0, 0, 0.35);
  }
  .steps .finale { font-style: italic; }
  .brand {
    position: absolute;
    left: 96px; top: 322px;
  }
  .brand-name {
    font-weight: 400;
    font-size: 63px;
    line-height: 70px;
    letter-spacing: 0.045em;
  }
  .brand-owner {
    font-style: italic;
    font-size: 41px;
    line-height: 50px;
    margin-top: 4px;
  }
  .services {
    position: absolute;
    left: 96px; top: 470px;
    width: 730px;
    font-size: 21px;
    line-height: 29px;
    letter-spacing: 0.02em;
  }
  .contact {
    position: absolute;
    left: 96px; top: 630px;
    list-style: none;
    font-size: 30px;
    line-height: 44px;
    letter-spacing: 0.01em;
  }
</style>
</head>
<body>
<main class="flier">
  <svg class="foliage" width="1200" height="848" viewBox="0 0 1200 848" role="img" aria-label="Silhouettes of ferns, leaves, tomatoes, chilli, carrot, herbs, leek and beetroot in dark greens along the top right and right edge">
    <defs>
      <linearGradient id="foliageTone" x1="0" y1="0" x2="0.3" y2="1">
        <stop offset="0" stop-color="#0f9448"/>
        <stop offset="0.55" stop-color="#11884a"/>
        <stop offset="1" stop-color="#146236"/>
      </linearGradient>
    </defs>
    <path fill="url(#foliageTone)" opacity="0.9"
      d="M550 30 H1172 V820 H840 C830 760 860 720 900 700 C930 640 980 600 1010 560 C1000 480 1010 420 1000 360 C930 330 860 310 810 280 C760 250 700 230 650 190 C610 150 570 100 550 30 Z"/>
  </svg>

  <div class="frame"></div>

  <p class="credential">
    <span class="level">CERTIFICATE III</span><br>
    <span class="course">Horticulture.</span><span class="college">FIELDSTONE COLLEGE</span>
  </p>

  <ul class="steps">
    <li>DESIGN</li>
    <li>INSTALL</li>
    <li>GROW</li>
    <li>TEND</li>
    <li class="finale">ENJOY!</li>
  </ul>

  <header class="brand">
    <h1 class="brand-name">KITCHEN PLOT GARDENS</h1>
    <p class="brand-owner">by Liam Hartley</p>
  </header>

  <p class="services">All your gardening and landscaping needs from design &amp; installation to general maintenance. Bespoke vegetable gardens and potager designs created to suite your site and requirments.</p>

  <ul class="contact">
    <li>Email: liam@kitchenplotgardens.com.au</li>
    <li>Mobile: 0400 182 365</li>
    <li>ABN: 51203948771</li>
  </ul>
</main>
</body>
</html>
```